2 Fold Brochure

We are a spa looking to create a professional elegant two fold brochure for a spa mainly black and white with a splash of lime green.
Look and feel: chic, modern, and spa-ish.

The front will include an image and also it should say: (somewhere under the photo) wherever you think it will look nice.
Skin Tightening
Cellulite Reduction
Body Contouring

The second Page:
Bipolar Radiofrequency(bolded): for immediate face lifting, tone and a complete new younger looking skin!
Multipolar Radiofrequency(bolded): with Vacuum system for body contour, cellulite and fat detachment from adipose tissue.
Cavitation with red LED to treat face and small areas of the body. Red LED light stimulates collagen synthesis.

Ultra Cavitation will sculpt, treat fat, cellulite and improve body shape! It does NOT involve surgery. There is no need for anesthesia, hospital stay or time off from work. Ultra cavitation will promote microscopic air bubbles to surround the lipocyte(fat cell) membranes and with its resonant frequency, the bubbles cause a high enough pressure to break up fat instantly. These broken lipocytes are then safely metabolized out of the human body.

PRESSOTHERAPY: A Complete Body Detox! Pressortherapy based on air pressure, promotes lymphatic drainage. It aslo has infrared system for body heat and electro muscle stimulation system.

Third Page:
Packages:

1. THE NEW FACELIFT:
*Skin Tightening
*Wrinkle Reduction
*Dark Circle Elimination
*Puffy Eye Relief

BODY SHAPING

2. BODY
*Fat Reduction
*Cellulite Reduction
*Body Firming

3. PRESSOTHERAPY (DETOX) $85
*Toxic Flushing
*Lymphatic Drainage
*Toning

5.POST PREGNANCY
*Fat Reduction
*Tummy Firming and Toning
*Cellulite Reduction
*Butt Toning

Buy 5 get 1 Free - $1,250
Buy 10 get 2 Free- $2,500

The back of the second page will include before and after photos I will be sending later. Also include the Logo in the front and by the prices. I have attached our logo.

Also we need a photo to place in the front. Something that shows face and body fat reduction.

```html
<!DOCTYPE html>
<html lang="en">
<head>
<meta charset="UTF-8">
<title>Lumen Day Spa – Brochure</title>
<link rel="stylesheet" href="https://fonts.googleapis.com/css2?family=Questrial&family=Didact+Gothic&display=swap">
<style>
  :root {
    --lime: #8cc63f;
    --lime-soft: #a9d468;
    --ink: #1d1d1d;
    --grey: #555;
    --paper: #ffffff;
    --page-shade: #f2f2f2;
    --stage: #e6e4e4;
    --skin-light: #f1dccd;
    --skin-mid: #d9b49b;
    --denim: #6f8fb3;
  }
  * { box-sizing: border-box; margin: 0; padding: 0; }
  html, body { width: 1200px; height: 900px; overflow: hidden; }
  body {
    background: var(--stage);
    font-family: "Didact Gothic", sans-serif;
    color: var(--ink);
    position: relative;
  }
  .page {
    position: absolute;
    top: 180px;
    width: 380px;
    height: 540px;
    background: var(--paper);
    overflow: hidden;
    box-shadow: 0 4px 14px rgba(0,0,0,.12);
  }
  .cover { left: 20px; }
  .spread { position: absolute; top: 180px; left: 420px; width: 760px; height: 540px; box-shadow: 0 4px 14px rgba(0,0,0,.12); }
  .spread .page { top: 0; box-shadow: none; }
  .inside-left { left: 0; background: linear-gradient(90deg, var(--paper) 85%, var(--page-shade)); }
  .inside-right { left: 380px; background: linear-gradient(90deg, var(--page-shade), var(--paper) 15%); }

  .photo { position: absolute; }
  .shapes { position: absolute; inset: 0; }

  /* Cover */
  .cover .photo-body { left: 140px; top: 0; width: 240px; height: 330px;
    background: linear-gradient(160deg, var(--skin-light), var(--skin-mid) 60%, #f4f0ec); }
  .cover .photo-face { left: 22px; top: 130px; width: 150px; height: 200px;
    background: radial-gradient(ellipse at 50% 45%, var(--skin-light), var(--skin-mid) 70%, #b98a70); border-radius: 8px; }
  .brand { position: absolute; left: 22px; top: 22px; display: flex; align-items: center; gap: 8px; }
  .brand-dot { width: 44px; height: 44px; border-radius: 50%; background: var(--paper); border: 2px solid var(--ink); }
  .brand-name { font-family: "Questrial", sans-serif; font-size: 14px; color: var(--ink); letter-spacing: .5px; }
  .cover-services { position: absolute; right: 18px; bottom: 30px; width: 340px; list-style: none; text-align: right; }
  .cover-services li {
    font-family: "Questrial", sans-serif; font-size: 27px; letter-spacing: 1.5px;
    text-transform: uppercase; padding: 6px 0 4px; border-bottom: 1.5px solid var(--lime);
  }

  /* Inside left */
  .treatments { position: absolute; left: 120px; top: 40px; width: 240px; font-size: 11.5px; line-height: 1.3; color: var(--grey); }
  .treatments p { margin-bottom: 12px; }
  .treatments strong { color: var(--ink); font-weight: normal; font-family: "Questrial", sans-serif; font-size: 13px; }
  .treatments h3 { font-family: "Questrial", sans-serif; font-weight: normal; font-size: 16px; color: var(--ink); margin-top: 6px; }
  .treatments .tagline { color: var(--ink); font-size: 13px; margin-bottom: 6px; }
  .inside-left .photo-face { left: 0; top: 350px; width: 130px; height: 190px;
    background: radial-gradient(ellipse at 60% 45%, var(--skin-light), var(--skin-mid) 70%, #c99f86); }

  /* Inside right */
  .packages-badge {
    position: absolute; right: 20px; top: -40px; width: 160px; height: 160px; border-radius: 50%;
    background: var(--lime); display: flex; align-items: flex-end; justify-content: center; padding-bottom: 34px;
    font-family: "Questrial", sans-serif; font-size: 22px; letter-spacing: 1px; color: var(--ink);
  }
  .package-list { position: absolute; left: 18px; top: 26px; width: 230px; list-style: none; }
  .package { padding-bottom: 14px; margin-bottom: 16px; border-bottom: 1.5px solid var(--lime); }
  .package:last-child { border-bottom: none; }
  .package h2 {
    font-family: "Questrial", sans-serif; font-weight: normal; font-size: 16px; text-transform: uppercase;
    display: flex; align-items: center; gap: 6px; margin-bottom: 8px;
  }
  .package h2::before { content: ""; width: 8px; height: 8px; border-radius: 50%; background: var(--lime); }
  .package ul { list-style: none; padding-left: 22px; font-size: 10.5px; line-height: 1.5; color: var(--grey); }
  .offers { position: absolute; left: 18px; bottom: 26px; font-family: "Questrial", sans-serif; font-size: 14px; line-height: 1.6; }
  .inside-right .photo-torso { left: 250px; top: 110px; width: 130px; height: 380px;
    background: linear-gradient(180deg, var(--skin-light) 0%, var(--skin-mid) 55%, var(--denim) 60%, #55739a 100%); }
</style>
</head>
<body>

  <section class="page cover">
    <div class="photo photo-body" role="img" aria-label="Slim woman's waist and hips in white underwear with a tape measure"></div>
    <svg class="shapes" viewBox="0 0 380 540" aria-hidden="true">
      <path d="M0 0 H150 C110 40 110 120 150 150 L0 150 Z" fill="#ffffff"/>
      <path d="M150 0 C110 40 110 120 150 150" fill="none" stroke="#8cc63f" stroke-width="14"/>
      <path d="M0 300 C80 360 200 370 380 300 V540 H0 Z" fill="#ffffff"/>
      <path d="M0 300 C80 360 200 370 380 300" fill="none" stroke="#8cc63f" stroke-width="18"/>
    </svg>
    <div class="photo photo-face" role="img" aria-label="Portrait of a smiling woman touching her smooth cheek"></div>
    <div class="brand">
      <span class="brand-dot"></span>
      <span class="brand-name">Lumen Day Spa</span>
    </div>
    <ul class="cover-services">
      <li>Skin Tightening</li>
      <li>Body Contouring</li>
      <li>Cellulite Reduction</li>
    </ul>
  </section>

  <div class="spread">
    <section class="page inside-left">
      <svg class="shapes" viewBox="0 0 380 540" aria-hidden="true">
        <circle cx="40" cy="360" r="70" fill="#8cc63f"/>
      </svg>
      <div class="photo photo-face" role="img" aria-label="Woman's face with lifting arrows drawn along the jawline and neck"></div>
      <div class="treatments">
        <p><strong>Bipolar Radiofrequency:</strong> for immediate face lifting, tone and a complete new younger looking skin!</p>
        <p><strong>Multipolar Radiofrequency:</strong> with Vacuum system for body contour, cellulite and fat detachment from adipose tissue. Cavitation with red LED to treat face and small areas of the body. Red LED light stimulates collagen synthesis.</p>
        <p><strong>Ultra Cavitation</strong> will sculpt, treat fat, cellulite and improve body shape! It does NOT involve surgery. There is no need for anesthesia, hospital stay or time off from work. Ultra cavitation will promote microscopic air bubbles to surround the lipocyte (fat cell) membranes and with its resonant frequency, the bubbles cause a high enough pressure to break up fat instantly. These broken lipocytes are then safely metabolized out of the human body.</p>
        <h3>PRESSOTHERAPY</h3>
        <p class="tagline">A Complete Body Detox!</p>
        <p>Pressotherapy based on air pressure, promotes lymphatic drainage. It also has infrared system for body heat and electro muscle stimulation system.</p>
      </div>
    </section>

    <section class="page inside-right">
      <div class="photo photo-torso" role="img" aria-label="Slim woman in oversized jeans showing her fat reduction"></div>
      <div class="packages-badge">PACKAGES</div>
      <ul class="package-list">
        <li class="package">
          <h2>The New Facelift</h2>
          <ul><li>Wrinkle Reduction</li><li>Skin Tightening</li><li>Dark Circle Elimination</li><li>Puffy Eye Relief</li></ul>
        </li>
        <li class="package">
          <h2>Body</h2>
          <ul><li>Fat Reduction</li><li>Cellulite Reduction</li><li>Body Firming</li></ul>
        </li>
        <li class="package">
          <h2>Pressotherapy</h2>
          <ul><li>Toning</li><li>Lymphatic Draining</li><li>Toxic Flushing</li></ul>
        </li>
        <li class="package">
          <h2>Post Pregnancy</h2>
          <ul><li>Fat Reduction</li><li>Tummy Firming and Toning</li><li>Cellulite Reduction</li><li>Butt Toning</li></ul>
        </li>
      </ul>
      <div class="offers">
        <p>Buy 5 get 1 Free - $1,250</p>
        <p>Buy 10 get 2 Free - $2,250</p>
      </div>
    </section>
  </div>

</body>
</html>
```